Grill & Ale Room requires web site design - Casual restaurant

Need website designed for re-branding of Restaurant based in Fort Morgan, Colorado. We offer a wide variety of American cuisine in a casual, rustic atmosphere. We're offering 16 craft beers on draft, as well as a full service bar, and modern, interesting menu selections in a friendly, fun and energetic environment, with an emphasis on superior customer service and high quality, locally sourced food. We are a family, and community service oriented establishment. The website design should convey a welcoming sense, "simplicity", yet sophisticated - without pretentiousness. The website should effectively convey our "home style" relaxed atmosphere, as well as our casual character.

Business Hours: Sunday - Thursday, 11am-10pm / Friday & Saturday, 11am-11am

The Rook Grill & Ale Room
2276 Kettering Lane
Fort Morgan, Colorado 80701
B: (970) 555-0174

WEBSITE ADDRESS: therookaleroom.example

Reason: Continuing to refine top submissions.

Reason: Submissions are still accepted, while refining several potential designs.

Target Market(s)

Young Adults
Families
Blue and White Collar Americans
Senior Citizens
Small town location, appeal to everyone

Industry/Entity Type

American Restaurant

Contact Information for Business Card

Dale L Ferris
Food & Beverage Director
2276 Kettering Lane
B: (970) 555-0174
M: (231) 555-0196
dlferris@rookaleroom.example
www.therookaleroom.example
***Use logo in uploaded files
***Open to single OR double sided
*** I will have additional names and information to add to this, for other employees.

Coding

Coded - Design and coding required

Number of Pages Required

5+ page

Font styles to use
Serif
Sans Serif
Decorative
Other font styles liked:
• Calafornian FB,

Requirements
Must have
• Home/Welcome Page
• Menu Page/Online Ordering Ready
• About Us/Contact Us page
• Catering/Private Events/Banquets Advertising section
• Ability to link to Facebook/TripAdvisor/Yelp/Instagram etc.
• Logo uploaded, reference for colors as well.
Nice to have
• About craft beer page
• Our Story/Bio section
• Photo Gallery
• Employment/Apply section
Should not have
• We are NOT a "fine dining" restaurant... think casual...

```html
<!DOCTYPE html>
<html lang="en">
<head>
<meta charset="utf-8">
<title>The Rook Grill &amp; Ale Room</title>
<link href="https://fonts.googleapis.com/css2?family=Crimson+Text:wght@400;600&family=Open+Sans:wght@400;600;700&display=swap" rel="stylesheet">
<style>
:root{
  --accent:#c2561b;
  --accent-dark:#a8470f;
  --ink:#2b2b2b;
  --muted:#555;
  --black:#0d0d0d;
  --header-top:#ffffff;
  --header-bottom:#e4e4e4;
  --rule:#d6d6d6;
  --white:#fff;
  --serif:'Crimson Text', Georgia, serif;
  --sans:'Open Sans', Arial, sans-serif;
}
*{box-sizing:border-box;margin:0;padding:0}
html,body{width:1200px;height:2579px;overflow:hidden}
body{position:relative;background:var(--white);font-family:var(--sans);color:var(--ink)}
.abs{position:absolute}

/* top bar */
.topbar{left:0;top:0;width:1200px;height:34px;background:var(--black);color:#fff}
.topbar .call{position:absolute;right:112px;top:7px;font-size:12px;display:flex;align-items:center;gap:8px}
.topbar .call b{font-family:var(--serif);font-size:20px;font-weight:400;letter-spacing:.5px}

/* header */
.site-header{left:0;top:34px;width:1200px;height:143px;background:linear-gradient(var(--header-top),var(--header-bottom))}
.brand{position:absolute;left:98px;top:40px;display:flex;align-items:center;gap:10px;font-family:var(--serif);font-size:46px;font-weight:600;color:var(--ink);line-height:1}
.brand .dot{width:14px;height:14px;border-radius:50%;background:var(--accent)}
.brand small{display:block;font-size:15px;font-weight:600;color:var(--ink);letter-spacing:.5px;margin-top:4px}
.main-nav{position:absolute;top:62px;left:464px;display:flex;font-family:var(--serif);font-size:16px;color:#333}
.main-nav a{color:inherit;text-decoration:none;margin-right:33px;position:relative}
.main-nav a.active{color:var(--accent);background:#fff;padding:6px 14px;margin:-6px 24px 0 0;height:30px}
.main-nav a.active::after{content:"";position:absolute;left:50%;top:30px;margin-left:-9px;width:18px;height:22px;background:var(--accent);clip-path:polygon(0 0,100% 0,100% 100%,50% 75%,0 100%)}

/* hero */
.hero{left:0;top:177px;width:1200px;height:574px;background:radial-gradient(ellipse at 50% 35%,#6a4a2c 0%,#3f2a19 45%,#1e140c 100%)}
.hero .arrow{position:absolute;top:270px;color:#fff;font-size:22px}
.hero-copy{position:absolute;left:0;width:1200px;top:196px;text-align:center;color:#fff}
.hero-copy h1{font-family:var(--serif);font-weight:400;font-size:40px;line-height:1}
.hero-copy h1 span{font-size:68px}
.hero-copy h2{font-family:var(--serif);font-weight:400;font-size:38px;margin-top:4px}
.hero-copy .rule{width:240px;height:1px;background:rgba(255,255,255,.7);margin:6px auto 16px}
.hero-copy p{font-size:15px;width:720px;margin:0 auto;line-height:1.25}
.btn{display:inline-block;background:var(--accent);color:#fff;font-family:var(--serif);font-size:20px;padding:6px 24px;margin-top:28px;width:148px;height:40px}

/* section titles */
.section-title{left:0;width:1200px;text-align:center;font-family:var(--serif);font-weight:400;font-size:34px;color:var(--accent)}
.marker{width:18px;height:26px;background:var(--accent);clip-path:polygon(0 0,100% 0,100% 100%,50% 72%,0 100%)}

/* menu cards */
.dish{width:238px;text-align:center;top:825px}
.dish .photo{height:181px}
.dish h3{font-family:var(--serif);font-weight:600;font-size:17px;color:var(--accent);margin-top:24px;letter-spacing:.3px}
.dish p{font-size:12px;color:var(--muted);line-height:20px;margin-top:2px}
.dish .price{font-weight:700;font-size:24px;color:var(--accent);margin-top:12px}
.dish .line{height:2px;background:var(--rule);margin-top:14px}
.photo-fries{background:linear-gradient(135deg,#e8b450,#c9802c)}
.photo-sprouts{background:radial-gradient(circle,#7a8a32,#3b2e1d)}
.photo-dip{background:radial-gradient(circle,#e9e3cf 40%,#8a6e4e)}
.photo-zucchini{background:linear-gradient(135deg,#b78a2e,#4c3a1c)}
.order-tag{position:absolute;left:66px;top:74px;background:var(--accent);color:#fff;font-family:var(--serif);font-size:14px;padding:3px 14px}

/* gallery */
.g-big{left:98px;top:1262px;width:413px;height:431px;background:linear-gradient(135deg,#5a3a22,#2a1a10)}
.g1{left:524px;top:1262px;width:279px;height:208px;background:radial-gradient(circle,#7c4a24,#24140a)}
.g2{left:820px;top:1262px;width:280px;height:208px;background:radial-gradient(circle,#4d7a2c,#6a4b2d)}
.g3{left:524px;top:1487px;width:279px;height:206px;background:linear-gradient(#4a3a44,#8a7a70)}
.g4{left:820px;top:1487px;width:280px;height:206px;background:radial-gradient(circle,#efe7d6 35%,#8a6a42)}
.g-big .arr{position:absolute;top:200px;color:#fff;font-size:20px}

/* about */
.about{left:0;top:1741px;width:1200px;height:528px;background:linear-gradient(90deg,#3a2418,#2a1c14 50%,#3d2a20);color:#fff;text-align:center}
.about h2{font-family:var(--serif);font-weight:400;font-size:34px;margin-top:42px}
.about .bm{margin:10px auto 0;width:22px;height:28px}
.about .lead{width:700px;margin:26px auto 0;font-size:12.5px;line-height:22px}
.avatar{width:82px;height:82px;border-radius:50%;background:linear-gradient(#c9a489,#7a5a48);border:3px solid #fff;margin:44px auto 0}
.about .q{font-size:26px;font-weight:700;line-height:1;margin-top:10px}
.about .quote{width:640px;margin:4px auto 0;font-size:12.5px;line-height:21px}
.about .who{font-family:var(--serif);font-style:italic;font-size:16px;margin-top:12px}

/* footer */
.site-footer{left:0;top:2269px;width:1200px;height:275px}
.col{position:absolute;top:26px}
.col h4{font-family:var(--serif);font-weight:400;font-size:29px;color:#333;margin-bottom:16px}
.col p,.col li{font-size:12.5px;line-height:26px;color:#333;list-style:none}
.col li::before{content:"›";margin-right:16px;color:#555}
.col li.on{color:var(--accent)}
.ico{display:inline-block;vertical-align:middle;margin-right:10px}
.newsletter{margin-top:6px;width:228px;height:34px;border:1px solid #ccc;box-shadow:0 2px 3px rgba(0,0,0,.15);font-size:12px;padding:8px 12px;position:relative;color:#333}
.newsletter svg{position:absolute;right:10px;top:10px}
.social{display:flex;gap:8px}
.social span{width:30px;height:30px;border-radius:50%}
.foot-brand{margin-top:32px;font-family:var(--serif);font-weight:600;font-size:34px;color:#333;display:flex;align-items:center;gap:8px}
.foot-brand .dot{width:10px;height:10px;border-radius:50%;background:var(--accent)}
.copybar{left:0;top:2544px;width:1200px;height:35px;background:var(--black);color:#bbb;font-size:11px;text-align:center;line-height:35px}
</style>
</head>
<body>

<div class="abs topbar">
  <div class="call">
    <svg width="12" height="12" viewBox="0 0 24 24"><path fill="#fff" d="M6.6 10.8a15 15 0 0 0 6.6 6.6l2.2-2.2a1 1 0 0 1 1-.25 11.4 11.4 0 0 0 3.6.57 1 1 0 0 1 1 1V20a1 1 0 0 1-1 1A17 17 0 0 1 3 4a1 1 0 0 1 1-1h3.5a1 1 0 0 1 1 1c0 1.25.2 2.45.57 3.57a1 1 0 0 1-.25 1z"/></svg>
    Call &amp; Book Now : <b>(970) 555-0174</b>
  </div>
</div>

<header class="abs site-header">
  <div class="brand"><span class="dot"></span><div>The Rook<small>Grill &amp; Ale Room</small></div></div>
  <nav class="main-nav">
    <a class="active" href="#">Home</a>
    <a href="#">Menu</a>
    <a href="#">Online Order</a>
    <a href="#">About us</a>
    <a href="#">Private Events</a>
    <a href="#">Banquets</a>
    <a href="#">Contact us</a>
  </nav>
</header>

<section class="abs hero" role="img" aria-label="Warm photo of friends dining together under string lights">
  <span class="arrow" style="left:12px">‹</span>
  <span class="arrow" style="right:12px">›</span>
  <div class="hero-copy">
    <h1>We offer a wide variety <span>of American</span></h1>
    <h2>cuisine in a casual, rustic atmosphere.</h2>
    <div class="rule"></div>
    <p>We're offering 16 craft beers on draft, as well as a full service bar, and modern, interesting menu selections in a friendly, fun and energetic environment.</p>
    <span class="btn">Order Now</span>
  </div>
</section>

<div class="abs marker" style="left:591px;top:751px"></div>
<h2 class="abs section-title" style="top:774px">Menus</h2>

<article class="abs dish" style="left:101px">
  <div class="photo photo-fries" role="img" aria-label="Queso loaded fries" style="position:relative"><span class="order-tag">Order Now</span></div>
  <h3>QUESO LOADED FRITES</h3>
  <p>crispy fries / bacon / pico de gallo<br>queso sauce / chipotle ranch</p>
  <div class="price">$8.99</div><div class="line"></div>
</article>
<article class="abs dish" style="left:355px">
  <div class="photo photo-sprouts" role="img" aria-label="Bowl of brussels sprouts"></div>
  <h3>BRUSSELS SPROUTS</h3>
  <p>flash fried / hickory bacon<br>crispy onion / maple soy glaze</p>
  <div class="price">$7.99</div><div class="line"></div>
</article>
<article class="abs dish" style="left:608px">
  <div class="photo photo-dip" role="img" aria-label="Bacon spinach dip"></div>
  <h3>BACON SPIN DIP</h3>
  <p>baked mozzarella / artichoke hearts<br>fresh vegetables / french bread</p>
  <div class="price">$9.99</div><div class="line"></div>
</article>
<article class="abs dish" style="left:861px">
  <div class="photo photo-zucchini" role="img" aria-label="Fried zucchini with dipping sauce"></div>
  <h3>FRIED ZUCCHINI</h3>
  <p>lightly breaded &amp; flash fried<br>served with horseradish cream</p>
  <div class="price">$7.99</div><div class="line"></div>
</article>

<div class="abs marker" style="left:591px;top:1172px"></div>
<h2 class="abs section-title" style="top:1200px">Gallery</h2>

<div class="abs g-big" role="img" aria-label="Friends toasting at a dinner table"><span class="arr" style="left:10px">‹</span><span class="arr" style="right:10px">›</span></div>
<div class="abs g1" role="img" aria-label="Busy restaurant dining room"></div>
<div class="abs g2" role="img" aria-label="Fresh green salad in a wooden bowl"></div>
<div class="abs g3" role="img" aria-label="Kitchen cooking pots"></div>
<div class="abs g4" role="img" aria-label="Plated pasta salad"></div>

<section class="abs about" role="img" aria-label="Dim photo of the bar interior behind the about text">
  <h2>About Us</h2>
  <svg class="bm" viewBox="0 0 22 28"><path d="M2 2h18v24l-9-7-9 7z" fill="none" stroke="#fff" stroke-width="2"/></svg>
  <p class="lead">Lorem ipsum dolor sit amet, consectetur adipiscing elit, sed do eiusmod tempor incididunt ut labore et dolore magna aliqua. Ut enim ad minim veniam, quis nostrud exercitation ullamco laboris nisi ut aliquip ex ea commodo consequat. Duis aute irure dolor in reprehenderit in voluptate velit esse cillum dolore eu fugiat nulla pariatur. Excepteur sint occaecat cupidatat non proident, sunt in culpa qui officia deserunt mollit anim id est laborum.</p>
  <div class="avatar" role="img" aria-label="Portrait of the chef"></div>
  <div class="q">&rdquo;</div>
  <p class="quote">Sed ut perspiciatis unde omnis iste natus error sit voluptatem accusantium doloremque laudantium, totam rem aperiam, eaque ipsa quae ab illo inventore veritatis et quasi architecto beatae vitae dicta</p>
  <div class="who">- Nora Whitley : Chef</div>
</section>

<footer class="abs site-footer">
  <div class="col" style="left:115px">
    <h4>Location</h4>
    <p><svg class="ico" width="10" height="14" viewBox="0 0 10 14"><path d="M5 0a5 5 0 0 0-5 5c0 4 5 9 5 9s5-5 5-9a5 5 0 0 0-5-5zm0 7a2 2 0 1 1 0-4 2 2 0 0 1 0 4z" fill="#333"/></svg>The Rook Grill &amp; Ale Room</p>
    <p style="padding-left:20px">2276 Kettering Lane<br>Fort Morgan, Colorado 80701<br>B: (970) 555-0174</p>
  </div>
  <div class="col" style="left:357px">
    <h4>Business Hours</h4>
    <p><svg class="ico" width="13" height="13" viewBox="0 0 14 14"><circle cx="7" cy="7" r="6" fill="#333"/><path d="M7 3v4h3" stroke="#fff" stroke-width="1.5" fill="none"/></svg>Sunday - Thursday, 11am-10pm</p>
    <p style="padding-left:23px;line-height:14px">Friday &amp; Saturday, 11am-11am</p>
    <h4 style="margin:22px 0 4px">Newsletter</h4>
    <div class="newsletter">Enter Email id<svg width="14" height="14" viewBox="0 0 14 14"><path d="M1 7l12-6-4 12-2-5z" fill="#333"/></svg></div>
  </div>
  <div class="col" style="left:650px">
    <h4>Quick Links</h4>
    <ul>
      <li class="on">Home</li><li>Menu</li><li>Online Order</li><li>About us</li><li>Private Events</li><li>Banquets</li><li>Contact us</li>
    </ul>
  </div>
  <div class="col" style="left:885px">
    <h4>Follow Us</h4>
    <div class="social">
      <span style="background:#2d4a8a"></span><span style="background:#2a9fd8"></span><span style="background:#c8302a"></span><span style="background:#b88a52"></span>
    </div>
    <div class="foot-brand"><span class="dot"></span>The Rook</div>
  </div>
</footer>

<div class="abs copybar">Copyrights © 2017, www.therookaleroom.example. All Rights Reserved.</div>

</body>
</html>
```